Business Card Design Project

Business card for law firm
Use existing logo
Must have:
Delmar R. Pennick
3721-C West 14th
Brenfield, TX 78599
dpennick@bvlawgroup.example
www.bvlawgroup.example
555-555-0143

Target Market(s)

Clients and potential clients, generally adult, business background

Industry/Entity Type

Business

Requirements
Must have
• Our logo, see below

```html
<!DOCTYPE html>
<html lang="en">
<head>
<meta charset="utf-8">
<title>Beckford Vance — Business Card</title>
<link rel="stylesheet" href="https://fonts.googleapis.com/css2?family=Cinzel:wght@400;700&display=swap">
<style>
  :root {
    --backdrop: #d3d4d6;
    --card-grey: #88898b;
    --card-white: #ffffff;
    --ink-light: #f4f4f4;
    --ink-dark: #262626;
    --ink-mid: #7a7a7a;
    --rule-light: #b4b5b7;
    --rule-dark: #9a9a9a;
    --mark-light: #d9d9d9;
    --mark-dark: #3a3a3a;
  }
  * { margin: 0; padding: 0; box-sizing: border-box; }
  html, body {
    width: 1200px; height: 743px; overflow: hidden;
    background: var(--backdrop);
    font-family: "Cinzel", "Times New Roman", serif;
  }
  .card {
    position: absolute; top: 198px;
    width: 511px; height: 331px;
  }
  .card--front { left: 53px; background: var(--card-grey); color: var(--ink-light); text-align: center; }
  .card--back { left: 631px; background: var(--card-white); }

  .front-mark {
    position: absolute; left: 230px; top: 77px;
    width: 51px; height: 51px; background: var(--mark-light);
  }
  .holder-name {
    position: absolute; left: 0; right: 0; top: 146px;
    font-size: 24px; font-weight: 400; letter-spacing: 1px; line-height: 1;
  }
  .holder-rule {
    position: absolute; left: 118px; width: 280px; top: 179px;
    height: 1px; background: var(--rule-light);
  }
  .contact {
    position: absolute; left: 0; right: 0; top: 187px;
    font-size: 17px; line-height: 21px;
  }
  .contact .sep { font-size: 10px; vertical-align: 3px; padding: 0 6px; }

  .firm {
    position: absolute; left: 50px; top: 142px;
    display: flex; align-items: flex-start; gap: 8px;
  }
  .firm-mark { width: 50px; height: 50px; background: var(--mark-dark); }
  .firm-text { width: 352px; }
  .firm-name {
    font-size: 31px; font-weight: 400; line-height: 30px; color: var(--ink-dark);
    letter-spacing: 0.5px; white-space: nowrap;
  }
  .firm-rule { height: 1px; background: var(--rule-dark); margin-top: 4px; }
  .firm-tagline {
    font-size: 13.5px; color: var(--ink-mid); letter-spacing: 0.6px;
    margin-top: 2px; white-space: nowrap;
  }
  .website {
    position: absolute; left: 0; right: 0; top: 287px; text-align: center;
    font-size: 11.5px; font-weight: 700; color: var(--ink-dark); letter-spacing: 0.3px;
  }
</style>
</head>
<body>
  <section class="card card--front">
    <div class="front-mark" aria-hidden="true"></div>
    <h1 class="holder-name">Delmar R. Pennick</h1>
    <div class="holder-rule"></div>
    <p class="contact">
      3721-C West 14th<span class="sep">•</span>Brenfield<span class="sep">•</span>TX 78599<br>
      dpennick@bvlawgroup.example<br>
      555-555-0143
    </p>
  </section>

  <section class="card card--back">
    <div class="firm">
      <div class="firm-mark" aria-hidden="true"></div>
      <div class="firm-text">
        <div class="firm-name">Beckford Vance</div>
        <div class="firm-rule"></div>
        <div class="firm-tagline">Attorneys and Counselors</div>
      </div>
    </div>
    <p class="website">www.bvlawgroup.example</p>
  </section>
</body>
</html>
```